Renewable energy website needs a wordpress website

We are a Renewable Energy company specialising in Energy Management, LED Lights and Solar PV Systems based in Kuala Lumpur.
We need wordpress website designed to match our company identity.
We would like to stick with similar shades of blue & green as our logo and to keep it fresh and creative at the same time.

```html
<!DOCTYPE html>
<html lang="en">
<head>
<meta charset="utf-8">
<title>Greenleaf Energy — Website Design</title>
<link href="https://fonts.googleapis.com/css2?family=Open+Sans:wght@300;400;600;700&display=swap" rel="stylesheet">
<style>
:root{
  --cyan:#1bd0ec;
  --cyan-dim:#1695a6;
  --ink:#333;
  --muted:#777;
  --light:#f1f1f1;
  --line:#dcdcdc;
  --dark:#262626;
  --white:#fff;
  --shade:rgba(0,0,0,.58);
}
*{box-sizing:border-box;margin:0;padding:0}
html,body{width:1200px;height:1045px;overflow:hidden;background:var(--white);font-family:"Open Sans",Arial,sans-serif;color:var(--ink)}
.board{position:relative;width:1200px;height:1045px;background:var(--white)}
.abs{position:absolute}

/* ---------- main page ---------- */
.page{position:absolute;left:53px;top:33px;width:463px;height:982px;background:var(--white);overflow:hidden;box-shadow:0 4px 18px rgba(0,0,0,.45)}
.site-header{position:absolute;left:0;top:0;width:100%;height:23px;background:var(--white)}
.brand{position:absolute;left:84px;top:5px;display:flex;align-items:center;gap:4px;font-size:7px;font-weight:700;color:var(--cyan-dim);letter-spacing:.3px}
.brand-dot{width:10px;height:10px;border-radius:50%;background:var(--cyan)}
.nav{position:absolute;left:208px;top:8px;display:flex;gap:8px;font-size:4.6px;font-weight:700;color:#444}
.nav-search{width:7px;height:5px;border:1px solid var(--cyan);border-radius:50%;margin-top:-1px}

.hero{position:absolute;left:0;top:23px;width:100%;height:170px;background:linear-gradient(180deg,#3b4450 0%,#5b6670 45%,#626a52 80%,#4c5436 100%)}
.hero-brand{position:absolute;left:0;width:100%;top:48px;text-align:center;font-size:11px;font-weight:700;color:var(--white);letter-spacing:1px}
.hero-brand span{display:inline-block;width:12px;height:12px;border-radius:50%;background:var(--cyan);vertical-align:-2px;margin-right:4px}
.hero-title{position:absolute;left:0;width:100%;top:84px;text-align:center;font-size:7px;font-weight:700;color:var(--white);letter-spacing:.8px}
.hero-sub{position:absolute;left:0;width:100%;top:94px;text-align:center;font-size:7px;font-weight:300;color:var(--white);letter-spacing:.6px}
.hero-note{position:absolute;left:0;width:100%;top:122px;text-align:center;font-size:3.6px;color:#ddd}
.hero-dots{position:absolute;left:0;width:100%;top:137px;text-align:center;font-size:0}
.hero-dots i{display:inline-block;width:2.5px;height:2.5px;border-radius:50%;background:#ccc;margin:0 2px}
.hero-dots i.on{background:var(--white)}
.chev{position:absolute}

.section-title{position:absolute;left:0;width:100%;text-align:center;font-size:6px;font-weight:700;color:#222;letter-spacing:.3px}
.section-title::before{content:"";display:block;width:18px;height:1px;background:var(--cyan);margin:0 auto 2px}

.grey-band{position:absolute;left:0;width:100%;background:var(--light)}
.filters{position:absolute;left:0;width:100%;top:211px;display:flex;justify-content:center;gap:8px}
.filter{font-size:3.6px;font-weight:700;background:#e4e4e4;color:#333;padding:2px 4px}
.filter.on{background:#333;color:var(--white)}
.tile{position:absolute;width:67px;height:67px}
.tile.wind{background:linear-gradient(180deg,#3f6db6 0%,#7fa6d8 55%,#6a8f3c 80%,#4f6a2a 100%)}
.tile.led{background:radial-gradient(circle at 40% 45%,#3a8a4a 0%,#1a2a5a 45%,#0a0a14 100%)}
.tile.solar{background:linear-gradient(160deg,#b9cde6 0%,#6a7f99 45%,#2f3d52 100%)}
.tile.active{outline:1px solid var(--cyan)}
.tile-hover{position:absolute;left:10px;top:10px;width:47px;height:47px;border-radius:50%;background:rgba(27,208,236,.85);text-align:center;color:var(--white);font-size:3.2px;font-weight:700;padding-top:9px;line-height:5px}

.col-head{position:absolute;width:80px;text-align:center;font-size:5px;font-weight:300;color:#555;letter-spacing:.3px}
.col-text{position:absolute;width:80px;text-align:center;font-size:3.6px;line-height:5.2px;color:var(--muted)}

.photo-band{position:absolute;left:0;width:100%;background:linear-gradient(180deg,#7d93aa 0%,#9cb0a6 40%,#5f7a3a 70%,#3f5424 100%)}
.card{position:absolute;background:#eeeeee;padding:7px 7px 0 30px}
.card svg{position:absolute;left:8px;top:8px}
.card h4{font-size:4.6px;font-weight:700;color:#333;letter-spacing:.3px;margin:4px 0 3px}
.card p{font-size:3.4px;line-height:4.8px;color:var(--muted)}
.order{position:absolute;left:0;width:100%;top:673px;text-align:center;font-size:12px;font-weight:400;color:var(--white);line-height:16px}
.btn{position:absolute;background:var(--cyan);color:var(--white);font-size:3.8px;font-weight:700;text-align:center;letter-spacing:.3px}

.contact{position:absolute;left:0;top:807px;width:100%;height:91px;background:var(--light)}
.label-head{position:absolute;font-size:5px;font-weight:700;color:#222}
.label-head::before{content:"";display:block;width:14px;height:1px;background:var(--cyan);margin-bottom:2px}
.field{position:absolute;background:var(--white);font-size:3.6px;color:#888;padding:1.5px 3px}
.team-label{position:absolute;font-size:3.8px;color:#555}
.team-photo{position:absolute;width:18px;height:18px;background:linear-gradient(180deg,#9a9a9a,#555)}
.team-photo.on{background:linear-gradient(180deg,#46d9f0,#1aa9c0)}
.cta-band{position:absolute;left:0;top:898px;width:100%;height:35px;background:var(--cyan);text-align:center;color:var(--white);font-size:6px;font-weight:700;letter-spacing:.6px;line-height:35px}
.cta-band span{font-weight:300}
.site-footer{position:absolute;left:0;top:933px;width:100%;height:49px;background:var(--dark)}
.foot-row{position:absolute;left:86px;right:86px;top:7px;display:flex;justify-content:space-between;font-size:3.6px;color:#aaa}

/* ---------- captions ---------- */
.caption{position:absolute;font-size:17px;font-weight:300;color:#222;text-decoration:underline;text-underline-offset:3px;white-space:nowrap}

/* ---------- popup screens ---------- */
.screen{position:absolute;left:598px;width:533px;overflow:hidden;background:var(--white);box-shadow:0 2px 8px rgba(0,0,0,.3)}
.screen .overlay{position:absolute;inset:0;background:var(--shade)}
.modal{position:absolute;left:156px;width:221px;background:var(--white);text-align:center}
.modal-arrow{position:absolute;top:40px}
.modal h5{position:absolute;left:0;width:100%;font-size:6.5px;font-weight:400;color:#444}
.modal p{position:absolute;left:14px;right:14px;font-size:3.6px;line-height:5px;color:#666}
.modal .more{position:absolute;right:10px;font-size:4.4px;color:#444;text-decoration:underline}
.s-tile{position:absolute;width:82px;height:76px}
</style>
</head>
<body>
<div class="board">

  <!-- ===== Main page ===== -->
  <div class="page">
    <header class="site-header">
      <div class="brand"><span class="brand-dot"></span>GREENLEAF ENERGY</div>
      <nav class="nav"><span>ENERGY MANAGEMENT</span><span>LED LIGHTS</span><span>SOLAR PV SYSTEMS</span><span>CONTACTS</span><span>TEAM</span><span class="nav-search"></span></nav>
    </header>

    <section class="hero" role="img" aria-label="Wind turbines on green hills under a cloudy sky">
      <div class="hero-brand"><span></span>GREENLEAF ENERGY</div>
      <div class="hero-title">RENEABLE ENERGY SYSTEMS</div>
      <div class="hero-sub">BECAUSE WE CARE</div>
      <div class="hero-note">scroll to see more</div>
      <div class="hero-dots"><i></i><i class="on"></i><i></i></div>
      <svg class="abs" style="left:40px;top:62px" width="8" height="14" viewBox="0 0 8 14"><path d="M7 1L1 7l6 6" fill="none" stroke="#fff" stroke-width="1"/></svg>
      <svg class="abs" style="left:312px;top:62px" width="8" height="14" viewBox="0 0 8 14"><path d="M1 1l6 6-6 6" fill="none" stroke="#fff" stroke-width="1"/></svg>
    </section>
    <svg class="chev" style="left:0;top:165px" width="463" height="30" viewBox="0 0 463 30"><polygon points="0,0 231.5,28 463,0 463,30 0,30" fill="#fff"/></svg>

    <div class="grey-band" style="top:266px;height:112px"></div>
    <svg class="chev" style="left:0;top:377px" width="463" height="16" viewBox="0 0 463 16"><polygon points="0,0 463,0 231.5,14" fill="#f1f1f1"/></svg>

    <h2 class="section-title" style="top:202px">OUR PROJECTS</h2>
    <div class="filters"><span class="filter">ENERGY MANAGEMENT</span><span class="filter">LED LIGHTS</span><span class="filter">SOLAR PV SYSTEMS</span><span class="filter on">ALL</span></div>

    <div class="tile wind" style="left:87px;top:231px" role="img" aria-label="Wind turbines on a hillside"></div>
    <div class="tile led" style="left:162px;top:231px" role="img" aria-label="Colourful LED light strands"></div>
    <div class="tile solar active" style="left:237px;top:231px" role="img" aria-label="Rows of solar panels">
      <div class="tile-hover">
        <svg width="8" height="8" viewBox="0 0 8 8"><circle cx="3.3" cy="3.3" r="2.4" fill="none" stroke="#fff" stroke-width=".8"/><path d="M5 5l2.4 2.4" stroke="#fff" stroke-width=".8"/></svg><br>VIEW PROJECT<br>SOLAR BATTERIES
      </div>
    </div>
    <div class="tile solar" style="left:312px;top:231px" role="img" aria-label="Solar panels under a bright sky"></div>
    <div class="tile solar" style="left:87px;top:307px" role="img" aria-label="Solar panel array"></div>
    <div class="tile wind" style="left:162px;top:307px" role="img" aria-label="Wind turbine in a field"></div>
    <div class="tile led" style="left:237px;top:307px" role="img" aria-label="LED lights glowing at night"></div>
    <div class="tile solar" style="left:312px;top:307px" role="img" aria-label="Solar panels on a rooftop"></div>

    <h2 class="section-title" style="top:412px">ENERGY MANAGEMENT</h2>
    <div class="col-head" style="left:86px;top:433px">TEAM</div>
    <div class="col-head" style="left:191px;top:433px">CLIENTS</div>
    <div class="col-head" style="left:297px;top:433px">WORK</div>
    <p class="col-text" style="left:86px;top:444px">We audit buildings and track every kilowatt, then plan simple changes that cut waste, lower monthly bills and keep your sites running cleaner through the whole year.</p>
    <p class="col-text" style="left:191px;top:444px">Offices, hotels, factories and schools across the region trust our team to measure usage, advise on upgrades and report clear savings after every single project.</p>
    <p class="col-text" style="left:297px;top:444px">Our work covers metering, smart controls, lighting retrofits and rooftop solar, all installed by certified engineers and backed by friendly support long after handover.</p>

    <div class="photo-band" style="top:620px;height:100px" role="img" aria-label="Green countryside with wind turbines on the horizon"></div>
    <svg class="chev" style="left:0;top:700px" width="463" height="24" viewBox="0 0 463 24"><polygon points="0,0 231.5,22 463,0 463,24 0,24" fill="#fff"/></svg>

    <h2 class="section-title" style="top:517px">LED LIGHTS</h2>
    <div class="card" style="left:88px;top:538px;width:137px;height:50px">
      <svg width="15" height="15" viewBox="0 0 15 15"><circle cx="7.5" cy="7.5" r="6.5" fill="none" stroke="#1bd0ec" stroke-width="1"/><path d="M4.5 7.7l2 2 4-4.4" fill="none" stroke="#1bd0ec" stroke-width="1"/></svg>
      <h4>LED LIGHTS FOR HOME</h4><p>Bright, efficient LED fittings for every room at home, using less power and lasting for many years without fuss.</p>
    </div>
    <div class="card" style="left:238px;top:538px;width:139px;height:50px">
      <svg width="15" height="15" viewBox="0 0 15 15"><circle cx="7.5" cy="7.5" r="6.5" fill="none" stroke="#1bd0ec" stroke-width="1"/><path d="M4.5 7.7l2 2 4-4.4" fill="none" stroke="#1bd0ec" stroke-width="1"/></svg>
      <h4>LED FOR BUSINESS</h4><p>Commercial LED panels and high bay lights that cut running costs for shops, warehouses and busy offices.</p>
    </div>
    <div class="card" style="left:88px;top:601px;width:137px;height:50px">
      <svg width="15" height="15" viewBox="0 0 15 15"><circle cx="7.5" cy="7.5" r="6.5" fill="none" stroke="#1bd0ec" stroke-width="1"/><path d="M4.5 7.7l2 2 4-4.4" fill="none" stroke="#1bd0ec" stroke-width="1"/></svg>
      <h4>WHOW IT WORKS</h4><p>We survey your space, suggest the right lamps, install them quickly and show you the savings each month.</p>
    </div>
    <div class="card" style="left:238px;top:601px;width:139px;height:50px">
      <svg width="15" height="15" viewBox="0 0 15 15"><circle cx="7.5" cy="7.5" r="6.5" fill="none" stroke="#1bd0ec" stroke-width="1"/><path d="M4.5 7.7l2 2 4-4.4" fill="none" stroke="#1bd0ec" stroke-width="1"/></svg>
      <h4>DEALERS</h4><p>Become a partner and offer our full LED range to your own customers with trade prices and training.</p>
    </div>

    <div class="order">Want to order?</div>
    <div class="btn" style="left:205px;top:699px;width:53px;height:10px;line-height:10px">CONTACT US</div>

    <h2 class="section-title" style="top:735px">SOLAR PV SYSTEMS</h2>
    <div class="col-head" style="left:86px;top:755px">TEAM</div>
    <div class="col-head" style="left:191px;top:755px">CLIENTS</div>
    <div class="col-head" style="left:297px;top:755px">WORK</div>
    <p class="col-text" style="left:86px;top:766px">We audit buildings and track every kilowatt, then plan simple changes that cut waste, lower monthly bills and keep your sites running cleaner through the whole year.</p>
    <p class="col-text" style="left:191px;top:766px">Offices, hotels, factories and schools across the region trust our team to measure usage, advise on upgrades and report clear savings after every single project.</p>
    <p class="col-text" style="left:297px;top:766px">Our work covers metering, smart controls, lighting retrofits and rooftop solar, all installed by certified engineers and backed by friendly support long after handover.</p>

    <section class="contact">
      <div class="label-head" style="left:87px;top:9px">CONTACT US</div>
      <div class="field" style="left:87px;top:26px;width:83px;height:9px">Name</div>
      <div class="field" style="left:87px;top:40px;width:83px;height:9px">Email</div>
      <div class="field" style="left:87px;top:55px;width:83px;height:9px">Phone</div>
      <div class="field" style="left:182px;top:26px;width:105px;height:38px">Comments</div>
      <div class="btn" style="left:243px;top:68px;width:44px;height:11px;line-height:11px">SEND LETTER</div>
      <div class="team-label" style="left:305px;top:12px">OUR TEAM</div>
      <div class="team-photo" style="left:305px;top:26px" role="img" aria-label="Team member portrait"></div>
      <div class="team-photo on" style="left:332px;top:26px" role="img" aria-label="Selected team member portrait"></div>
      <div class="team-photo" style="left:360px;top:26px" role="img" aria-label="Team member portrait"></div>
      <div class="team-photo" style="left:305px;top:47px" role="img" aria-label="Team member portrait"></div>
      <div class="team-photo" style="left:332px;top:47px" role="img" aria-label="Team member portrait"></div>
      <div class="team-photo" style="left:360px;top:47px" role="img" aria-label="Team member portrait"></div>
    </section>
    <div class="cta-band">USE RENEABLE ENERGY SYSTEMS, <span>HELP THE PLANET</span></div>
    <footer class="site-footer"><div class="foot-row"><span>12 JALAN HIJAU, KL</span><span>INFO@GREENLEAFENERGY.COM</span><span>(03) 2100 4578</span></div></footer>
  </div>

  <!-- ===== Captions ===== -->
  <div class="caption" style="left:607px;top:153px">This window appears when you click on a project picture</div>
  <div class="caption" style="left:548px;top:558px">This window appears when you click on one of team member’s photo</div>

  <!-- ===== Project popup ===== -->
  <div class="screen" style="top:205px;height:320px">
    <svg class="abs" style="left:0;top:0" width="533" height="16" viewBox="0 0 533 16"><polygon points="0,0 533,0 266.5,14" fill="#5b6670"/></svg>
    <h2 class="section-title" style="top:34px">OUR PROJECTS</h2>
    <div class="abs" style="left:0;width:100%;top:49px;display:flex;justify-content:center;gap:9px"><span class="filter">ENERGY MANAGEMENT</span><span class="filter">LED LIGHTS</span><span class="filter">SOLAR PV SYSTEMS</span><span class="filter on">ALL</span></div>
    <div class="s-tile tile wind" style="left:0;top:67px" role="img" aria-label="Wind turbines on a hillside"></div>
    <div class="s-tile tile led" style="left:90px;top:67px" role="img" aria-label="Colourful LED lights"></div>
    <div class="s-tile tile solar" style="left:360px;top:67px" role="img" aria-label="Solar panels"></div>
    <div class="s-tile tile solar" style="left:450px;top:67px" role="img" aria-label="Solar panels"></div>
    <div class="s-tile tile solar" style="left:0;top:152px" role="img" aria-label="Solar panel array"></div>
    <div class="s-tile tile solar" style="left:450px;top:152px" role="img" aria-label="Solar panel array"></div>
    <h2 class="section-title" style="top:274px">ENERGY MANAGEMENT</h2>
    <div class="col-head" style="left:60px;top:296px;width:100px">TEAM</div>
    <div class="col-head" style="left:216px;top:296px;width:100px">CLIENTS</div>
    <div class="col-head" style="left:372px;top:296px;width:100px">WORK</div>
    <div class="overlay"></div>
    <div class="modal" style="top:59px;height:167px">
      <div class="abs" style="left:43px;top:8px;width:138px;height:97px;background:linear-gradient(160deg,#9fc0e6 0%,#5f7fa6 40%,#2c3a4e 80%,#8a8f7a 100%)" role="img" aria-label="Large solar battery panels in a field"></div>
      <svg class="modal-arrow" style="left:10px" width="6" height="14" viewBox="0 0 6 14"><path d="M5 1L1 7l4 6" fill="none" stroke="#1bd0ec" stroke-width=".8"/></svg>
      <svg class="modal-arrow" style="right:10px" width="6" height="14" viewBox="0 0 6 14"><path d="M1 1l4 6-4 6" fill="none" stroke="#1bd0ec" stroke-width=".8"/></svg>
      <h5 style="top:111px">Solar Bataries</h5>
      <p style="top:124px">High capacity storage keeps solar power ready for the evening, so your building draws less from the grid and more from the sun.</p>
      <span class="more" style="top:155px">Learn more</span>
    </div>
  </div>

  <!-- ===== Team popup ===== -->
  <div class="screen" style="top:607px;height:305px">
    <h2 class="section-title" style="top:19px">SOLAR PV SYSTEMS</h2>
    <div class="col-head" style="left:0;top:44px;width:100px">TEAM</div>
    <div class="col-head" style="left:216px;top:44px;width:100px">CLIENTS</div>
    <div class="col-head" style="left:420px;top:44px;width:100px">WORK</div>
    <p class="col-text" style="left:0;top:55px;width:150px">We audit buildings and track every kilowatt, then plan simple changes that cut waste, lower monthly bills and keep your sites running cleaner through the whole year.</p>
    <p class="col-text" style="left:192px;top:55px;width:150px">Offices, hotels, factories and schools across the region trust our team to measure usage, advise on upgrades and report clear savings after every single project.</p>
    <p class="col-text" style="left:385px;top:55px;width:148px">Our work covers metering, smart controls, lighting retrofits and rooftop solar, all installed by certified engineers and backed by friendly support long after handover.</p>
    <div class="abs" style="left:0;top:140px;width:100%;height:106px;background:var(--light)"></div>
    <div class="label-head" style="left:0;top:150px">CONTACT US</div>
    <div class="field" style="left:0;top:174px;width:112px;height:11px">Name</div>
    <div class="field" style="left:0;top:190px;width:112px;height:11px">Email</div>
    <div class="field" style="left:0;top:206px;width:112px;height:11px">Phone</div>
    <div class="btn" style="left:278px;top:222px;width:50px;height:12px;line-height:12px">SEND LETTER</div>
    <div class="team-photo" style="left:378px;top:176px;width:21px;height:21px" role="img" aria-label="Team member portrait"></div>
    <div class="team-photo on" style="left:404px;top:176px;width:21px;height:21px" role="img" aria-label="Team member portrait"></div>
    <div class="team-photo" style="left:430px;top:176px;width:21px;height:21px" role="img" aria-label="Team member portrait"></div>
    <div class="team-photo" style="left:404px;top:200px;width:21px;height:21px" role="img" aria-label="Team member portrait"></div>
    <div class="team-photo" style="left:430px;top:200px;width:21px;height:21px" role="img" aria-label="Team member portrait"></div>
    <div class="abs" style="left:0;top:246px;width:100%;height:38px;background:var(--cyan);text-align:center;line-height:38px;color:#fff;font-size:7px;font-weight:700;letter-spacing:.6px">USE RENEABLE ENERGY SYSTEMS, <span style="font-weight:300">HELP THE PLANET</span></div>
    <div class="abs" style="left:0;top:284px;width:100%;height:21px;background:var(--dark)"><div class="foot-row" style="left:100px;right:100px;top:8px;font-size:4px"><span>12 JALAN HIJAU, KL</span><span>INFO@GREENLEAFENERGY.COM</span><span>(03) 2100 4578</span></div></div>
    <div class="overlay"></div>
    <div class="modal" style="top:47px;height:166px">
      <div class="abs" style="left:61px;top:5px;width:97px;height:96px;background:linear-gradient(180deg,#e9e9e9 0%,#b5b5b5 55%,#3a3a3a 100%)" role="img" aria-label="Portrait photo of the sales manager"></div>
      <svg class="modal-arrow" style="left:10px" width="6" height="14" viewBox="0 0 6 14"><path d="M5 1L1 7l4 6" fill="none" stroke="#1bd0ec" stroke-width=".8"/></svg>
      <svg class="modal-arrow" style="right:10px" width="6" height="14" viewBox="0 0 6 14"><path d="M1 1l4 6-4 6" fill="none" stroke="#1bd0ec" stroke-width=".8"/></svg>
      <h5 style="top:108px">Sales Manager</h5>
      <p style="top:121px">Leads our sales team and helps every client choose the right system, from first call to final installation and ongoing support.</p>
      <span class="more" style="top:153px">Contact us</span>
    </div>
  </div>

</div>
</body>
</html>
```